Enterprise Application UI beautification

We have an enterprise application that is being redesigned. A screenshot from the new UX/UI is provided. The current UI design is OK but we would like it to look better. The key goals of the UI are to look like a premium product (think luxury brand) and for it to be visually very appealing/attractive. When people see the UI we want them to have a significant, positive reaction. They should "ooh" and "ahh". This is a product sold to large enterprises, not consumers. The current UI is a little plain. The colors we want to use are blue, yellow, black, white and gray. We probably don't want different colors but feel free to use any variations within or close to that color scheme that you see fit. Also feel free to modify the spacing, icons, widgets, tables, fonts, etc.

Target Market(s)

Large enterprise customers (Meridian 300).

Number of Pages Required

1 page

Font styles to use
Sans Serif

Colors
3277b5

Requirements
Must have
• A premium feel.

```html
<!DOCTYPE html>
<html lang="en">
<head>
<meta charset="utf-8">
<title>Data Sources</title>
<link href="https://fonts.googleapis.com/css2?family=Exo+2:wght@300;400&display=swap" rel="stylesheet">
<style>
:root{
  --ink:#2b3440;
  --sidebar:#2d3e50;
  --rail:#223140;
  --active:#285a74;
  --accent:#1fa3c9;
  --link:#4a8fd6;
  --green:#1bb08a;
  --page:#f6f7fa;
  --card:#ffffff;
  --band:#c3d6f4;
  --line:#dde2e8;
}
*{box-sizing:border-box;margin:0;padding:0}
html,body{width:1200px;height:814px;overflow:hidden}
body{font-family:"Exo 2",sans-serif;font-weight:300;color:var(--ink);background:var(--page);position:relative}
.topbar{position:absolute;left:0;top:0;width:1200px;height:54px;background:#fff;border-bottom:1px solid #e2e6ea}
.brand{position:absolute;left:0;top:0;width:65px;height:54px;border-right:1px solid #e2e6ea;display:flex;align-items:center;justify-content:center;gap:4px;font-size:11px;font-weight:400;color:var(--sidebar)}
.brand .dot{width:7px;height:7px;border-radius:50%;background:var(--sidebar)}
.search{position:absolute;left:65px;top:0;width:269px;height:54px;border-right:1px solid #e2e6ea;padding-left:24px;font-size:16px;line-height:54px;color:#444}
.search svg{position:absolute;right:26px;top:19px}
.user{position:absolute;right:70px;top:0;height:54px;display:flex;align-items:center;gap:10px;font-size:16px;color:#333}
.sidebar{position:absolute;left:0;top:54px;width:334px;height:760px;background:var(--sidebar)}
.rail{position:absolute;left:14px;top:75px;width:58px;height:439px;background:var(--rail);border-radius:4px}
.rail svg{position:absolute;left:16px}
.side-title{position:absolute;left:87px;top:22px;font-size:23px;color:#fff;white-space:nowrap}
.add{position:absolute;left:252px;top:26px;width:62px;height:22px;background:var(--green);color:#fff;font-size:12px;font-weight:400;text-align:center;line-height:22px;border-radius:2px}
.source{position:absolute;left:87px;width:222px;height:48px;padding:8px 0 0 12px;white-space:nowrap}
.source .name{font-size:14px;color:#fff}
.source .type{font-size:10px;color:#c7d0d9;margin-top:1px}
.source.active{background:var(--active);border-right:4px solid var(--accent)}
.title-row{position:absolute;left:362px;top:76px;display:flex;align-items:center;gap:30px;white-space:nowrap}
.page-title{font-size:22px;font-weight:300;color:#333}
.actions{display:flex;gap:22px;font-size:11.5px;color:var(--link);margin-top:4px}
.actions span{display:flex;align-items:center;gap:5px}
.info{position:absolute;left:362px;top:128px;width:800px;height:120px;background:var(--card);border:1px solid #e6e9ee;border-radius:3px}
.info div{position:absolute;font-size:14px;white-space:nowrap}
.section-title{position:absolute;left:362px;top:281px;font-size:23px;font-weight:300;color:#333}
.panel{position:absolute;left:361px;width:805px;background:var(--card);border-radius:3px;box-shadow:0 1px 4px rgba(0,0,0,.09)}
.panel-head{position:absolute;left:19px;display:flex;align-items:center;gap:6px;font-size:14px;color:var(--link)}
.chip{width:15px;height:15px;border-radius:50%;background:#eef2f7;display:flex;align-items:center;justify-content:center;font-size:10px;color:var(--link);font-weight:400}
.table{position:absolute;left:7px;top:46px;width:789px}
.table .head{height:32px;background:var(--band);border-radius:3px;font-size:14px;font-weight:400}
.table .row{height:23px;border-bottom:1px solid var(--line);font-size:14px}
.table .row:last-child{border-bottom:none}
.table .c1{position:absolute;left:26px}
.table .c2{position:absolute;left:197px}
.table .head,.table .row{position:relative;display:flex;align-items:center}
</style>
</head>
<body>
<header class="topbar">
  <div class="brand"><span class="dot"></span>Corvane</div>
  <div class="search">Search
    <svg width="16" height="16" viewBox="0 0 16 16"><circle cx="6.5" cy="6.5" r="5" fill="none" stroke="#555" stroke-width="1.8"/><path d="M10 10l5 5" stroke="#555" stroke-width="2"/></svg>
  </div>
  <div class="user">
    <svg width="18" height="18" viewBox="0 0 18 18"><circle cx="9" cy="9" r="5.5" fill="none" stroke="#333" stroke-width="2"/><circle cx="9" cy="9" r="2" fill="#333"/><g stroke="#333" stroke-width="2.4"><path d="M9 0v3M9 15v3M0 9h3M15 9h3M2.6 2.6l2.1 2.1M13.3 13.3l2.1 2.1M2.6 15.4l2.1-2.1M13.3 4.7l2.1-2.1"/></g></svg>
    Dana Holt
    <svg width="14" height="10" viewBox="0 0 14 10"><path d="M1 2l6 6 6-6" fill="none" stroke="#333" stroke-width="2.2"/></svg>
  </div>
</header>

<aside class="sidebar">
  <div class="rail">
    <svg style="top:29px" width="26" height="22" viewBox="0 0 26 22" fill="none" stroke="#56677a" stroke-width="1.4"><circle cx="7" cy="6" r="3"/><circle cx="19" cy="6" r="3"/><circle cx="13" cy="10" r="3"/><circle cx="7" cy="16" r="3"/><circle cx="19" cy="16" r="3"/></svg>
    <svg style="top:103px" width="26" height="18" viewBox="0 0 26 18" fill="none" stroke="#56677a" stroke-width="1.4"><path d="M6 16h15a4 4 0 0 0 0-8 7 7 0 0 0-13-1 5 5 0 0 0-2 9z"/></svg>
    <svg style="top:172px" width="24" height="22" viewBox="0 0 24 22" fill="none" stroke="#1fa3c9" stroke-width="2"><path d="M3 6l16-3-3 16c-4 0-9-1-12-3"/></svg>
    <svg style="top:242px" width="22" height="24" viewBox="0 0 22 24" fill="none" stroke="#56677a" stroke-width="1.4"><rect x="3" y="4" width="16" height="18" rx="2"/><rect x="8" y="2" width="6" height="4"/><path d="M8 15l3 2 4-6"/></svg>
    <svg style="top:315px" width="22" height="22" viewBox="0 0 22 22" fill="none" stroke="#56677a" stroke-width="1.4"><rect x="2" y="4" width="18" height="16"/><path d="M2 9h18M6 2v4M16 2v4M6 13h2M10 13h2M14 13h2M6 16h2M10 16h2M14 16h2"/></svg>
    <svg style="top:386px" width="22" height="22" viewBox="0 0 22 22" fill="none" stroke="#56677a" stroke-width="1.4"><path d="M6 18V6l-3 3M16 4v12l3-3M6 18h4M12 4h4"/></svg>
  </div>
  <div class="side-title">Data Sources</div>
  <div class="add">+ Add</div>
  <div class="source active" style="top:73px"><div class="name">Cloudforge - Sandbox</div><div class="type">Cloudforge.io</div></div>
  <div class="source" style="top:144px"><div class="name">TableStore Test 1 (administrator)</div><div class="type">TableStore SQL</div></div>
  <div class="source" style="top:216px"><div class="name">TableStore Test 2 (administrator)</div><div class="type">TableStore SQL</div></div>
  <div class="source" style="top:288px"><div class="name">Sadga</div><div class="type">Cloudforge.io</div></div>
  <div class="source" style="top:360px"><div class="name">Cloudforge Test 1 (masterd ev)</div><div class="type">TableStore SQL</div></div>
  <div class="source" style="top:432px"><div class="name">CFG - Field Entry Test</div><div class="type">Cloudforge.io</div></div>
  <div class="source" style="top:503px"><div class="name">CFG 44</div><div class="type">Cloudforge.io</div></div>
  <div class="source" style="top:574px"><div class="name">CFG 66</div><div class="type">Cloudforge.io</div></div>
</aside>

<main>
  <div class="title-row">
    <h1 class="page-title">Cloudforge - Sandbox</h1>
    <div class="actions">
      <span><svg width="12" height="12" viewBox="0 0 12 12" fill="none" stroke="#4a8fd6" stroke-width="1.2"><path d="M1 11l1-3 7-7 2 2-7 7z"/></svg>Edit</span>
      <span><svg width="16" height="12" viewBox="0 0 16 12" fill="none" stroke="#4a8fd6" stroke-width="1.2"><circle cx="6" cy="6" r="5" fill="#4a8fd6"/><circle cx="10" cy="6" r="5"/></svg>Clone</span>
      <span><svg width="10" height="10" viewBox="0 0 10 10" stroke="#4a8fd6" stroke-width="1.3"><path d="M1 1l8 8M9 1l-8 8"/></svg>Delete</span>
    </div>
  </div>

  <section class="info">
    <div style="left:32px;top:16px">Data Source Name</div><div style="left:209px;top:16px">Cloudforge - Sandbox</div>
    <div style="left:385px;top:16px">Username</div><div style="left:561px;top:16px">masterdev@dev.ridgeline.net</div>
    <div style="left:32px;top:40px">Status</div><div style="left:209px;top:40px">Active</div>
    <div style="left:385px;top:40px">Security Token</div><div style="left:561px;top:40px">tadkaji4234ifndkn3</div>
    <div style="left:32px;top:64px">Created By</div><div style="left:209px;top:64px">harlow.test</div>
    <div style="left:385px;top:64px">Environment Type</div><div style="left:561px;top:64px">Production</div>
    <div style="left:32px;top:88px">Last updated By</div><div style="left:209px;top:88px">harlow.test</div>
    <div style="left:385px;top:88px">Connected App</div><div style="left:561px;top:88px">No</div>
  </section>

  <h2 class="section-title">Data Objects</h2>

  <section class="panel" style="top:334px;height:181px">
    <div class="panel-head" style="top:16px"><span class="chip">⌄</span>Account<span class="chip">×</span><span style="margin-left:30px">Fields</span><span class="chip">+</span></div>
    <div class="table">
      <div class="head"><span class="c1">Field Name</span><span class="c2">Data Type</span></div>
      <div class="row"><span class="c1">Account description</span><span class="c2">Common Text</span></div>
      <div class="row"><span class="c1">Account Fax</span><span class="c2">Address. Address Line 3</span></div>
      <div class="row"><span class="c1">Account ID</span><span class="c2">Common ID</span></div>
      <div class="row"><span class="c1">Account Name</span><span class="c2">Address. Address Line 1</span></div>
    </div>
  </section>
  <section class="panel" style="top:523px;height:37px"><div class="panel-head" style="top:10px"><span class="chip">⌄</span>Asset<span class="chip">×</span></div></section>
  <section class="panel" style="top:569px;height:37px"><div class="panel-head" style="top:10px"><span class="chip">⌄</span>Asset Relationship<span class="chip">×</span></div></section>
  <section class="panel" style="top:614px;height:36px"><div class="panel-head" style="top:10px"><span class="chip">⌄</span>Asset Token Event<span class="chip">×</span></div></section>
  <section class="panel" style="top:659px;height:37px"><div class="panel-head" style="top:11px"><span class="chip">⌄</span>Case<span class="chip">×</span></div></section>
</main>
</body>
</html>
```